3D Printing Website redesign

We are in the process of redesigning our website. Attached is an image of one of the proposed pages - "The Brightlander". The idea with this page is that site visitors can get an indicative estimate of the cost of 3D Printing based on some provided metrics. When the user alters the metrics the price changes accordingly. We are looking for a design to support this page that will also be used across our site.

```html
<!DOCTYPE html>
<html lang="en">
<head>
<meta charset="utf-8">
<title>The Brightlander – Layerworks Studio</title>
<link rel="stylesheet" href="https://fonts.googleapis.com/css2?family=Lato:wght@300;400;700&display=swap">
<style>
:root{
  --topbar:#2d2d2d;
  --sky:#33b6ec;
  --navy:#1f4a97;
  --navy-text:#233e7d;
  --deep:#1c4f9c;
  --mid:#2f8fd6;
  --ink:#444;
  --muted:#888;
  --line:#c9c9c9;
  --panel:#ffffff;
  --bubble:#8ecbec;
  --submit:#0b8fe2;
  --band:#efefef;
  --foot:#f5f5f5;
}
*{box-sizing:border-box;margin:0;padding:0}
html,body{width:1050px;height:1200px;overflow:hidden}
body{font-family:'Lato',sans-serif;color:var(--ink);background:#fff;position:relative}
.abs{position:absolute}

/* top bar */
.topbar{left:0;top:0;width:1050px;height:40px;background:var(--topbar);color:#fff;font-size:13px}
.region-map{left:122px;top:5px;width:33px;height:28px;background:var(--sky);border-radius:40% 55% 45% 50%}
.region{left:164px;top:12px}
.contact{left:482px;top:11px;display:flex;align-items:center;gap:8px}
.login{left:840px;top:5px;width:72px;height:30px;background:var(--sky);color:#123;display:flex;align-items:center;justify-content:center;font-size:13px}

/* header */
.brand{left:0;top:40px;width:1050px;height:83px;background:#fff}
.brand-disc{left:313px;top:10px;width:136px;height:136px;border-radius:50%;background:#fff;z-index:3}
.brand-disc span{position:absolute;left:18px;top:18px;width:100px;height:100px;border-radius:50%;background:var(--navy)}
.brand-name{left:452px;top:58px;font-size:30px;font-weight:700;color:var(--navy);letter-spacing:1px;z-index:3}
.strip{left:0;top:123px;width:1050px;height:24px;background:var(--navy)}
.nav{left:0;top:147px;width:1050px;height:38px;background:var(--sky);display:flex;justify-content:center;align-items:center;gap:6px;color:#fff;font-size:15px;font-weight:300;letter-spacing:.3px}
.nav i{font-style:normal;opacity:.6}

/* hero */
.hero{left:0;top:185px;width:1050px;height:439px;background:radial-gradient(ellipse at 50% 45%,#3ea7e6 0%,var(--mid) 45%,var(--deep) 100%)}
.hero-title{left:0;top:210px;width:1050px;text-align:center;color:#fff;font-size:33px;font-weight:400;letter-spacing:.5px}
.tab-band{left:183px;top:282px;width:440px;height:49px;background:linear-gradient(90deg,#2f95d9,#4cc0ef)}
.tab-active{left:623px;top:262px;width:241px;height:70px;background:var(--panel)}
.tab{top:270px;display:flex;align-items:center;gap:16px;font-size:27px;font-weight:300;color:#fff}
.tab .icon{width:52px;height:52px;border-radius:50%;background:radial-gradient(circle at 40% 35%,#7ec6ef,#1c4f9c)}
.tab.on{color:var(--navy-text)}
.panel{left:183px;top:331px;width:681px;height:242px;background:var(--panel)}
.label{left:232px;font-size:13px;font-weight:700;color:#555}
.track{left:318px;width:203px;height:2px;background:var(--line)}
.knob{width:9px;height:16px;background:#1a8ad6;border:1px solid #0f6fb0}
.ends{top:392px;font-size:8px;color:var(--muted)}
.select{left:318px;top:507px;width:203px;height:24px;background:#f1f1ef;border:1px solid #ddd}
.select b{position:absolute;right:0;top:0;width:30px;height:22px;border-left:1px solid #ddd;background:#f7f7f7}
.bubble{left:654px;top:363px;width:164px;height:164px;border-radius:50%;background:var(--bubble);color:#6db6e0;font-size:80px;font-weight:700;display:flex;align-items:center;justify-content:center}
.total{left:623px;top:540px;width:226px;text-align:center;font-size:12px;font-weight:700;color:#333}
.lead{left:0;top:586px;width:1050px;text-align:center;color:#fff;font-size:19px;font-weight:300}

/* form */
.field{left:182px;width:327px;height:33px;border:1px solid var(--line);font-size:11px;color:#555;padding:11px 8px;background:#fff}
.note{left:532px;top:637px;font-size:11px;color:#555}
.captcha{left:533px;top:678px;width:155px;height:45px;background:linear-gradient(90deg,#b8c6dc,#d9e1ee);border:1px solid #999}
.ctrl{top:693px;font-size:12px;color:#555}
.check{left:529px;top:802px;width:18px;height:18px;border:1px solid #aaa;background:#f0f0f0}
.check-label{left:555px;top:803px;font-size:12px;color:#333}
.submit{left:528px;top:848px;width:326px;height:32px;background:linear-gradient(var(--sky),var(--submit));color:#fff;font-size:15px;display:flex;align-items:center;justify-content:center}
.foot-note{left:0;top:901px;width:1050px;text-align:center;font-size:10px;color:#555}

/* newsletter */
.news{left:0;top:932px;width:1050px;height:56px;background:var(--band);border-top:1px solid #e2e2e2;border-bottom:1px solid #e2e2e2}
.news-title{left:168px;top:947px;font-size:20px;font-weight:700;color:var(--navy-text)}
.news-ask{left:284px;top:947px;font-size:20px;font-weight:300;color:#666}
.news-input{left:600px;top:944px;width:263px;height:31px;background:#fff;border:1px solid var(--line);font-size:11px;color:#aaa;padding:9px 15px}

/* footer */
.footer{left:0;top:988px;width:1050px;height:170px;background:var(--foot)}
.col{top:1012px;font-size:9px;line-height:13.5px;color:#666}
.col h4{font-size:9px;color:var(--navy-text);font-weight:700}
.col h4.gap{margin-top:13px}
.foot-brand{left:640px;top:1005px;width:202px;height:140px;display:flex;flex-direction:column;align-items:center;justify-content:center;gap:10px}
.foot-brand span{width:90px;height:90px;border-radius:50%;background:var(--navy)}
.foot-brand b{font-size:19px;color:var(--navy);letter-spacing:.5px}
.bottom{left:0;top:1158px;width:1050px;height:42px;background:var(--navy);color:#fff}
.copy{left:168px;top:1173px;font-size:9px;color:#fff}
.follow{left:709px;top:1171px;font-size:12px;font-weight:700;color:#fff}
.social{top:1163px;width:30px;height:30px;border-radius:50%;background:#fff}
</style>
</head>
<body>

<div class="abs topbar"></div>
<div class="abs region-map" role="img" aria-label="Outline map of Australia"></div>
<div class="abs region" style="color:#fff;font-size:13px">Australia</div>
<div class="abs contact" style="color:#fff;font-size:13px">
  <svg width="20" height="20" viewBox="0 0 24 24" fill="none" stroke="#33b6ec" stroke-width="2"><path d="M5 3h4l2 5-3 2a11 11 0 0 0 6 6l2-3 5 2v4a2 2 0 0 1-2 2A17 17 0 0 1 3 5a2 2 0 0 1 2-2z"/></svg>
  <span>61 2 9000 4821 &nbsp;|&nbsp; 0400 555 218 &nbsp;|&nbsp; UAN &nbsp;222-333-444</span>
</div>
<div class="abs login">LOG IN</div>

<header class="abs brand"></header>
<div class="abs strip"></div>
<div class="abs brand-disc"><span></span></div>
<div class="abs brand-name">LAYERWORKS STUDIO</div>

<nav class="abs nav">
  <span>SHOP</span><i>/</i><span>WHAT WE DO</span><i>/</i><span>THE BRIGHTLANDER</span><i>/</i><span>MATERIALS</span><i>/</i><span>GALLERY</span><i>/</i><span>DIY</span><i>/</i><span>TRAINING</span><i>/</i><span>ABOUT US</span><i>/</i><span>BLOG</span>
</nav>

<section class="abs hero"></section>
<h1 class="abs hero-title">THE BRIGHTLANDER</h1>
<div class="abs tab-band"></div>
<div class="abs tab-active"></div>
<div class="abs tab" style="left:220px"><span class="icon" role="img" aria-label="Scanner icon"></span>SCAN</div>
<div class="abs tab" style="left:416px"><span class="icon" role="img" aria-label="Design grid icon"></span>DESIGN</div>
<div class="abs tab on" style="left:660px"><span class="icon" role="img" aria-label="Printer icon"></span>PRINT</div>

<div class="abs panel"></div>
<div class="abs label" style="top:377px">SHAPE</div>
<div class="abs track" style="top:381px"></div>
<div class="abs knob" style="left:341px;top:373px"></div>
<div class="abs ends" style="left:318px">SQUARE</div>
<div class="abs ends" style="left:478px">CIRCULAR</div>
<div class="abs label" style="top:425px">SIZE</div>
<div class="abs track" style="top:432px"></div>
<div class="abs knob" style="left:341px;top:424px"></div>
<div class="abs label" style="top:466px">VOLUME</div>
<div class="abs track" style="top:474px"></div>
<div class="abs knob" style="left:341px;top:466px"></div>
<div class="abs label" style="top:511px">MATERIAL</div>
<div class="abs select"><b><svg width="30" height="22" viewBox="0 0 30 22"><path d="M11 9h8l-4 5z" fill="#888"/></svg></b></div>
<div class="abs bubble">?</div>
<div class="abs total">BRIGHTLANDER TOTAL: $36*</div>
<p class="abs lead">For Further information and inquiries, Please fill in the form below:</p>

<div class="abs field" style="top:641px">NAME</div>
<div class="abs field" style="top:690px">EMAIL</div>
<div class="abs field" style="top:740px">PHONE</div>
<div class="abs field" style="top:790px;height:92px">INSTRUCTIONS</div>
<p class="abs note">Please enter the following text to the box below to continue.</p>
<div class="abs captcha" role="img" aria-label="Distorted verification text"></div>
<svg class="abs" style="left:698px;top:693px" width="12" height="12" viewBox="0 0 12 12" fill="none" stroke="#555" stroke-width="1.6"><path d="M10 6a4 4 0 1 1-1.2-2.8M9 1v3H6"/></svg>
<svg class="abs" style="left:716px;top:693px" width="14" height="12" viewBox="0 0 14 12" fill="#555"><path d="M1 4h3l4-3v10L4 8H1z"/><path d="M10 3q2 3 0 6" stroke="#555" fill="none"/></svg>
<div class="abs" style="left:740px;top:693px;width:12px;height:12px;background:#555;color:#fff;font-size:9px;font-weight:700;text-align:center;line-height:12px">?</div>
<div class="abs field" style="left:529px;top:740px"></div>
<div class="abs check"></div>
<div class="abs check-label">I would like to receive promotional material</div>
<div class="abs submit">SUBMIT</div>
<p class="abs foot-note">* Duis sed odio sit amet nibh vulputate cursus a sit amet mauris. Morbi accumsan ipsu velitincidunt auctor a orn.</p>

<div class="abs news"></div>
<div class="abs news-title">Newsletter</div>
<div class="abs news-ask">Want to receive our Newsletter?</div>
<div class="abs news-input">ENTER YOUR EMAIL</div>
<svg class="abs" style="left:815px;top:950px" width="38" height="20" viewBox="0 0 38 20" fill="none" stroke="#333" stroke-width="1.5"><path d="M2 3h8M5 7h5M8 11h2"/><rect x="14" y="2" width="22" height="15"/><path d="M14 2l11 9 11-9"/></svg>

<footer class="abs footer"></footer>
<div class="abs col" style="left:172px"><h4>Printing</h4>Quote<br>Technologies<h4 class="gap">Printers</h4>Machines for sale<br>Machines to rent<br>Servicing<br>Buy Materials</div>
<div class="abs col" style="left:317px"><h4>Materials</h4>Overview<br>Plastic<br>Powder<br>High-Detail Resin<br>Nylon<br>Wood<br>Rubber</div>
<div class="abs col" style="left:465px"><h4>Training</h4>Sydney 3D Printers<br>Meetup<br>Studio Workshops<h4 class="gap">Franchise</h4>Franchise Opportunity</div>
<div class="abs foot-brand"><span></span><b>LAYERWORKS STUDIO</b></div>

<div class="abs bottom"></div>
<div class="abs copy">COPYRIGHT © 2014 LAYERWORKS STUDIO &nbsp;&nbsp;|&nbsp;&nbsp; ALL RIGHTS RESERVED</div>
<div class="abs follow">Follow Us</div>
<div class="abs social" style="left:771px" aria-label="Social profile"></div>
<div class="abs social" style="left:805px" aria-label="Social profile"></div>

</body>
</html>
```